landscape and garden design business card

I would like a business card designed for my landscape and garden design company, Wrenfield Landscapes. We are located in Colorado. I would like to include our logo, contact info, and social media/web site address or QR code. Looking for an organic, flowing design that incorporates our logo.

Target Market(s)

Homeowners and businesses that need garden and landscape design

Contact Information for Business Card

Would like it to say landscape and garden design

Requirements
Must have
• Landscape and garden design

```html
<!DOCTYPE html>
<html lang="en">
<head>
<meta charset="utf-8">
<title>Wrenfield Landscapes – Business Card</title>
<link href="https://fonts.googleapis.com/css2?family=Lora:wght@400;500&display=swap" rel="stylesheet">
<style>
  :root {
    --forest: #1f3330;
    --sage: #bbbbab;
    --paper: #ffffff;
    --backdrop: #ecece9;
  }
  html, body {
    margin: 0;
    padding: 0;
    width: 1200px;
    height: 1200px;
    overflow: hidden;
    background: var(--backdrop);
  }
  .canvas {
    position: relative;
    width: 1200px;
    height: 1200px;
    font-family: "Lora", Georgia, serif;
  }
  .card {
    position: absolute;
    left: 200px;
    width: 800px;
    height: 480px;
    box-shadow: 0 6px 24px rgba(0,0,0,0.12);
  }
  .card-front { top: 80px; background: var(--forest); }
  .card-back { top: 600px; background: var(--paper); }
  .card svg { display: block; width: 800px; height: 480px; }
  .brand-text { font-family: "Lora", Georgia, serif; font-weight: 400; }
  .tagline { font-family: "Lora", Georgia, serif; font-weight: 500; letter-spacing: 2px; }
  .contact-text { font-family: "Lora", Georgia, serif; fill: var(--forest); }
</style>
</head>
<body>
<div class="canvas">

  <!-- Front of card -->
  <section class="card card-front" aria-label="Card front">
    <svg viewBox="0 0 800 480" xmlns="http://www.w3.org/2000/svg">
      <circle class="brand-mark" cx="400" cy="150" r="88" fill="var(--sage)"/>
      <text class="brand-text" x="400" y="305" text-anchor="middle" font-size="58" fill="var(--sage)">Wrenfield</text>
      <text class="brand-text" x="400" y="345" text-anchor="middle" font-size="26" fill="var(--sage)">Landscapes</text>
      <line x1="300" y1="372" x2="500" y2="372" stroke="var(--sage)" stroke-width="1"/>
      <text class="tagline" x="400" y="400" text-anchor="middle" font-size="16" fill="var(--sage)">LANDSCAPE AND GARDEN DESIGN</text>
    </svg>
  </section>

  <!-- Back of card -->
  <section class="card card-back" aria-label="Card back">
    <svg viewBox="0 0 800 480" xmlns="http://www.w3.org/2000/svg">
      <rect class="edge-stripe" x="0" y="0" width="32" height="480" fill="var(--forest)"/>

      <circle class="brand-mark" cx="210" cy="168" r="70" fill="var(--forest)"/>
      <text class="brand-text" x="210" y="296" text-anchor="middle" font-size="44" fill="var(--forest)">Wrenfield</text>
      <text class="brand-text" x="210" y="328" text-anchor="middle" font-size="22" fill="var(--forest)">Landscapes</text>
      <text class="tagline" x="210" y="360" text-anchor="middle" font-size="12" fill="var(--forest)" letter-spacing="1.5">LANDSCAPE AND GARDEN DESIGN</text>

      <path class="info-panel" fill="var(--forest)"
        d="M423 0 H800 V480 H423 V456 Q423 438 401 430 V50 Q423 42 423 24 Z"/>

      <path class="name-bar" fill="var(--sage)" d="M397 85 H800 V165 H397 A40 40 0 0 1 397 85 Z"/>
      <circle cx="397" cy="125" r="28" fill="none" stroke="var(--forest)" stroke-width="4"/>
      <circle cx="397" cy="116" r="8" fill="var(--forest)"/>
      <path d="M383 138 Q397 122 411 138 Z" fill="var(--forest)"/>
      <text class="contact-text" x="444" y="137" font-size="36">Your Name</text>

      <g class="contact-row">
        <rect x="417" y="195" width="383" height="57" fill="var(--sage)"/>
        <circle cx="457" cy="223" r="19" fill="none" stroke="var(--forest)" stroke-width="3"/>
        <path d="M449 219 Q457 211 465 219 L462 222 H452 Z M451 224 H463 V230 H451 Z" fill="var(--forest)"/>
        <text class="contact-text" x="490" y="231" font-size="22">+0123456789</text>
      </g>
      <g class="contact-row">
        <rect x="417" y="266" width="383" height="56" fill="var(--sage)"/>
        <circle cx="457" cy="294" r="19" fill="none" stroke="var(--forest)" stroke-width="3"/>
        <rect x="448" y="288" width="18" height="12" fill="var(--forest)"/>
        <path d="M448 288 L457 295 L466 288" fill="none" stroke="var(--sage)" stroke-width="1.5"/>
        <text class="contact-text" x="490" y="302" font-size="22">wrenfieldlandscapes</text>
      </g>
      <g class="contact-row">
        <rect x="417" y="337" width="383" height="60" fill="var(--sage)"/>
        <circle cx="457" cy="367" r="19" fill="none" stroke="var(--forest)" stroke-width="3"/>
        <circle cx="457" cy="367" r="10" fill="none" stroke="var(--forest)" stroke-width="2"/>
        <ellipse cx="457" cy="367" rx="4" ry="10" fill="none" stroke="var(--forest)" stroke-width="2"/>
        <line x1="447" y1="367" x2="467" y2="367" stroke="var(--forest)" stroke-width="2"/>
        <text class="contact-text" x="490" y="375" font-size="22">www.wrenfieldlandscapes</text>
      </g>
    </svg>
  </section>

</div>
</body>
</html>
```